Veltro Coaching Business Card

We need a business card designed for a a company called "Veltro Coaching". We offer consulting, coaching and training to business leaders and coaches (across the world) using the latest findings in neuroscience, social and emotional intelligence and positive psychology. The final design should communicate the use of brain science to create sustainable relationships.

The card should be doublesided. The logo is attached and names and titles will be provided to the successful designer. Thank you.

Industry/Entity Type

Training

```html
<!DOCTYPE html>
<html lang="en">
<head>
<meta charset="utf-8">
<title>Veltro Coaching – Business Card</title>
<link rel="stylesheet" href="https://fonts.googleapis.com/css2?family=Questrial&display=swap">
<style>
  :root {
    --stage: #d9d9d9;
    --card-blue: #1796cf;
    --card-blue-light: #2aaee3;
    --card-blue-dark: #0f7fb6;
    --paper: #ffffff;
    --paper-shade: #e6e6e6;
    --ink-white: #ffffff;
    --shadow: rgba(0, 0, 0, 0.18);
  }
  * { box-sizing: border-box; margin: 0; padding: 0; }
  html, body { width: 1200px; height: 871px; overflow: hidden; }
  body {
    background: var(--stage);
    font-family: "Questrial", "Century Gothic", sans-serif;
  }
  .canvas {
    position: relative;
    width: 1200px;
    height: 871px;
    display: flex;
    justify-content: center;
    align-items: center;
    gap: 70px;
  }
  .card {
    position: relative;
    width: 380px;
    height: 620px;
    border-radius: 0 46px 0 46px;
    overflow: hidden;
    box-shadow: 0 10px 30px var(--shadow);
  }

  /* Front */
  .card-front { background: var(--paper); }
  .front-brand {
    height: 280px;
    background: radial-gradient(ellipse at 50% 35%, var(--paper) 0%, var(--paper-shade) 100%);
    display: flex;
    align-items: center;
    justify-content: center;
    gap: 12px;
  }
  .front-details {
    height: 340px;
    background: radial-gradient(ellipse at 55% 40%, var(--card-blue-light) 0%, var(--card-blue) 55%, var(--card-blue-dark) 100%);
    color: var(--ink-white);
    padding: 40px 0 0 52px;
  }
  .person-name { font-size: 31px; letter-spacing: 0.3px; line-height: 1.1; }
  .person-title { font-size: 19px; margin-top: 6px; }
  .contact-list { list-style: none; margin-top: 44px; }
  .contact-list li {
    display: flex;
    align-items: center;
    gap: 12px;
    font-size: 17px;
    margin-bottom: 15px;
    padding-left: 26px;
  }
  .contact-list li.address { padding-left: 24px; gap: 0; }
  .contact-icon { width: 16px; height: 16px; flex: none; }

  /* Back */
  .card-back {
    background: radial-gradient(ellipse at 50% 40%, var(--card-blue-light) 0%, var(--card-blue) 55%, var(--card-blue-dark) 100%);
    display: flex;
    align-items: center;
    justify-content: center;
    gap: 14px;
  }

  /* Brand name */
  .brand-mark {
    width: 18px; height: 18px;
    border-radius: 50%;
    flex: none;
  }
  .brand-name {
    font-size: 34px;
    letter-spacing: 0.5px;
    line-height: 1;
  }
  .front-brand .brand-mark { background: var(--card-blue); }
  .front-brand .brand-name { color: var(--card-blue); }
  .card-back .brand-mark { background: var(--ink-white); }
  .card-back .brand-name { color: var(--ink-white); }
</style>
</head>
<body>
<main class="canvas">
  <section class="card card-front" aria-label="Card front">
    <div class="front-brand">
      <span class="brand-mark"></span>
      <span class="brand-name">Veltro Coaching</span>
    </div>
    <div class="front-details">
      <p class="person-name">Daniel Harper</p>
      <p class="person-title">Director</p>
      <ul class="contact-list">
        <li>
          <svg class="contact-icon" viewBox="0 0 16 16" aria-hidden="true">
            <path fill="#fff" d="M3.6 1.2l2.3 2.6-1.3 1.7c.9 2 2.1 3.3 4.1 4.3l1.6-1.3 2.6 2.3-1.2 2.2C7.4 12.9 2.6 8 1.4 3z"/>
          </svg>
          <span>555-012-347</span>
        </li>
        <li>
          <svg class="contact-icon" viewBox="0 0 16 16" aria-hidden="true">
            <rect x="1" y="3.5" width="14" height="10" rx="1" fill="#fff"/>
            <path d="M1.5 4.2L8 9l6.5-4.8" fill="none" stroke="#1796cf" stroke-width="1.3"/>
          </svg>
          <span>name@veltro.com</span>
        </li>
        <li>
          <svg class="contact-icon" viewBox="0 0 16 16" aria-hidden="true">
            <g fill="none" stroke="#fff" stroke-width="1.3">
              <circle cx="8" cy="8" r="6.5"/>
              <ellipse cx="8" cy="8" rx="2.8" ry="6.5"/>
              <path d="M1.5 8h13M2.6 4.6h10.8M2.6 11.4h10.8"/>
            </g>
          </svg>
          <span>www.veltro.com</span>
        </li>
        <li class="address"><span>Your Complete Address</span></li>
      </ul>
    </div>
  </section>

  <section class="card card-back" aria-label="Card back">
    <span class="brand-mark"></span>
    <span class="brand-name">Veltro Coaching</span>
  </section>
</main>
</body>
</html>
```